Word document template for sales proposals

I am after a template that is simple but impactful. Use of colour to be limited but some for impact would be good. The proposals are for use in the professional technical field.

```html
<!DOCTYPE html>
<html lang="en">
<head>
<meta charset="utf-8">
<title>Kestrel Works – Business Proposal Template</title>
<link rel="stylesheet" href="https://fonts.googleapis.com/css2?family=Montserrat:ital,wght@0,300;0,400;0,600;0,700;0,800;0,900;1,400&family=Open+Sans:wght@400;600&display=swap">
<style>
  :root{
    --orange:#f7931e;
    --blue:#29a3dc;
    --black:#000000;
    --white:#ffffff;
    --ink:#1a1a1a;
    --stage:#dedede;
    --photo-sky-a:#c9dde6;
    --photo-sky-b:#2f5865;
    --photo-warm-a:#8a6a4f;
    --photo-warm-b:#d8c3ad;
  }
  *{box-sizing:border-box;margin:0;padding:0}
  html,body{width:1200px;height:1200px;overflow:hidden;background:var(--stage)}
  body{position:relative;font-family:"Open Sans",Arial,sans-serif;color:var(--ink)}
  .icons{position:absolute;width:0;height:0}

  .page{position:absolute;width:538px;height:760px;background:var(--white);
    transform:scale(.621);transform-origin:0 0;overflow:hidden;
    box-shadow:0 4px 14px rgba(0,0,0,.25)}
  .page--cover{left:58px;top:110px}
  .page--about{left:432px;top:110px}
  .page--cooperation{left:805px;top:110px}
  .page--team{left:225px;top:625px}
  .page--closing{left:600px;top:625px}

  .shapes{position:absolute;left:0;top:0;width:538px;height:760px}

  .brand{position:absolute;font-family:"Montserrat",sans-serif;font-weight:800;
    font-size:15px;letter-spacing:1.5px;text-transform:uppercase;white-space:nowrap}
  .brand--cover{left:28px;top:64px;color:var(--orange)}
  .brand--band{left:40px;top:48px;color:var(--white);width:150px;text-align:center}

  .page-number{position:absolute;right:22px;top:40px;font-family:"Montserrat",sans-serif;
    font-weight:800;font-size:24px;color:var(--black)}

  .photo{position:absolute}

  /* cover / closing titles */
  .kicker{position:absolute;left:55px;top:458px;font-family:"Montserrat",sans-serif;
    font-weight:400;font-size:26px;color:var(--black)}
  .kicker-rule{position:absolute;height:2px;background:var(--orange)}
  .title-xl{position:absolute;left:54px;font-family:"Montserrat",sans-serif;
    font-weight:800;color:var(--black);line-height:.95}
  .accent-bar{position:absolute;left:55px;top:572px;width:58px;height:5px;background:var(--orange)}
  .lead{position:absolute;left:54px;width:375px;font-family:"Montserrat",sans-serif;
    font-size:11.2px;line-height:19px;color:#222}

  /* footers */
  .footer{position:absolute;left:0;bottom:0;width:538px;height:72px;
    font-family:"Montserrat",sans-serif;font-size:11.3px}
  .footer--dark{background:var(--black);color:var(--white)}
  .footer--orange{background:var(--orange);color:var(--ink)}
  .contact{position:absolute;display:flex;align-items:center;gap:13px;white-space:nowrap}
  .contact svg{width:14px;height:14px;fill:currentColor;flex:none}
  .contact--web{left:40px;top:15px}
  .contact--address{left:40px;top:40px}
  .contact--phone{left:305px;top:17px}
  .contact--mail{left:305px;top:41px}

  /* about */
  .section-heading{position:absolute;font-family:"Montserrat",sans-serif;font-weight:800;color:var(--black)}
  .about-heading{left:63px;top:350px;font-size:31px;line-height:36px}
  .column{position:absolute;font-size:10.6px;line-height:15px;text-align:justify;color:#222}
  .column--left{left:56px;top:467px;width:200px}
  .column--right{left:285px;top:467px;width:201px;font-size:9.8px;line-height:13.6px}

  /* cooperation */
  .coop-heading{left:55px;top:116px;font-size:27px;line-height:30px}
  .body-copy{position:absolute;left:55px;width:430px;font-size:9.8px;line-height:13.6px;text-align:justify;color:#222}
  .feature{position:absolute;top:552px;width:195px}
  .feature--one{left:55px}
  .feature--two{left:291px}
  .feature h3{display:flex;align-items:center;gap:14px;font-family:"Montserrat",sans-serif;
    font-weight:800;font-size:20px;color:var(--black);margin-bottom:8px}
  .feature h3::before{content:"";width:19px;height:19px;border-radius:50%;background:var(--black)}
  .feature p{font-size:9.8px;line-height:13.6px;text-align:justify;color:#222}

  /* team */
  .team-heading{left:0;width:538px;top:130px;text-align:center;font-size:27px}
  .member{position:absolute;width:134px;text-align:center;font-family:"Montserrat",sans-serif}
  .member .portrait{width:133px;height:138px}
  .member .name{margin-top:13px;font-weight:700;font-size:10.6px;color:var(--black)}
  .member .role{margin-top:4px;font-style:italic;font-size:10.6px;color:#333}
  .col-a{left:51px}.col-b{left:203px}.col-c{left:355px}
  .row-a{top:193px}.row-b{top:407px}
</style>
</head>
<body>

<svg class="icons" aria-hidden="true">
  <symbol id="i-globe" viewBox="0 0 16 16"><path d="M8 0a8 8 0 1 0 0 16A8 8 0 0 0 8 0zm5.9 7h-2.9a12 12 0 0 0-1-5 6 6 0 0 1 3.9 5zM8 2c.8 1 1.4 2.8 1.5 5h-3C6.6 4.8 7.2 3 8 2zM6 2a12 12 0 0 0-1 5H2.1A6 6 0 0 1 6 2zM2.1 9H5a12 12 0 0 0 1 5 6 6 0 0 1-3.9-5zM8 14c-.8-1-1.4-2.8-1.5-5h3c-.1 2.2-.7 4-1.5 5zm2 0a12 12 0 0 0 1-5h2.9A6 6 0 0 1 10 14z"/></symbol>
  <symbol id="i-pin" viewBox="0 0 16 16"><path d="M8 0a5.6 5.6 0 0 0-5.6 5.6C2.4 10 8 16 8 16s5.6-6 5.6-10.4A5.6 5.6 0 0 0 8 0zm0 8a2.4 2.4 0 1 1 0-4.8A2.4 2.4 0 0 1 8 8z"/></symbol>
  <symbol id="i-phone" viewBox="0 0 16 16"><path d="M3.6 1 6 3.5 4.8 5.6a9 9 0 0 0 5.6 5.6L12.5 10l2.5 2.4-1.6 2.6C7 15 1 9 1 2.6z"/></symbol>
  <symbol id="i-mail" viewBox="0 0 16 16"><path d="M1 3h14v1.2L8 8.6 1 4.2zm0 2.8 7 4.4 7-4.4V13H1z"/></symbol>
  <linearGradient id="g-sky" x1="0" y1="0" x2="1" y2="1"><stop offset="0" stop-color="#7a6a55"/><stop offset=".45" stop-color="#c9dde6"/><stop offset="1" stop-color="#2f5865"/></linearGradient>
</svg>

<!-- Page 1 : cover -->
<section class="page page--cover">
  <svg class="shapes" viewBox="0 0 538 760" aria-hidden="true">
    <polygon points="346,113 396,31 430,113" fill="var(--blue)"/>
    <polygon points="0,100 100,100 212,445 0,445" fill="var(--orange)"/>
    <polygon points="205,410 252,410 222,445" fill="var(--blue)"/>
  </svg>
  <svg class="photo" style="left:0;top:0" width="538" height="760" viewBox="0 0 538 760" role="img" aria-label="Photo: glass office tower seen from below with autumn trees">
    <polygon points="105,113 538,113 538,410 205,410" fill="url(#g-sky)"/>
  </svg>
  <svg class="shapes" viewBox="0 0 538 760" aria-hidden="true">
    <polygon points="396,31 456,31 538,165 538,282" fill="var(--orange)"/>
  </svg>
  <div class="brand brand--cover">Kestrel Works</div>
  <div class="kicker">Business</div>
  <div class="kicker-rule" style="left:198px;top:476px;width:75px"></div>
  <div class="title-xl" style="top:496px;font-size:46px">Proposal</div>
  <div class="accent-bar"></div>
  <p class="lead" style="top:592px">A magazine is a periodical publication, which can either be printed or published electronically. It is issued regularly, usually every week or every month, and it contains a variety of content.</p>
  <footer class="footer footer--dark">
    <span class="contact contact--web"><svg><use href="#i-globe"/></svg>www.kestrelworks.example</span>
    <span class="contact contact--address"><svg><use href="#i-pin"/></svg>48 Foundry Lane, Eastbrook</span>
    <span class="contact contact--phone"><svg><use href="#i-phone"/></svg>+1-555-014-2280</span>
    <span class="contact contact--mail"><svg><use href="#i-mail"/></svg>hello@kestrelworks.example</span>
  </footer>
</section>

<!-- Page 2 : about company -->
<section class="page page--about">
  <div class="photo" role="img" aria-label="Photo: team members bumping fists over a desk with laptops and papers" style="left:0;top:128px;width:538px;height:298px;background:linear-gradient(135deg,#5a4636,#a08a74 45%,#ded8d0 70%,#6b5644)"></div>
  <svg class="shapes" viewBox="0 0 538 760" aria-hidden="true">
    <polygon points="245,20 538,20 538,92 245,92" fill="var(--orange)"/>
    <polygon points="0,17 250,17 283,100 0,100" fill="var(--blue)"/>
    <polygon points="280,92 293,92 287,101" fill="var(--black)"/>
    <polygon points="310,17 322,0 330,17" fill="var(--black)"/>
    <polygon points="322,0 334,0 374,66 364,70" fill="var(--blue)"/>
    <polygon points="0,333 265,333 298,435 0,435" fill="var(--blue)"/>
    <polygon points="290,425 302,425 296,434" fill="var(--black)"/>
  </svg>
  <div class="brand brand--band">Kestrel Works</div>
  <div class="page-number">02</div>
  <h2 class="section-heading about-heading">About<br>Company</h2>
  <p class="column column--left">To create your own, choose a topic that interests you. It can be anything from fashion and beauty to travel and the news. Once you have your overall theme, you can start brainstorming the content. Just starting? Design a memorable masthead with an equally memorable name. This goes on the cover and sets up the branding for your entire magazine.</p>
  <p class="column column--right">A magazine is a periodical publication, which can either be printed or published electronically. It is issued regularly, usually every week or every month, and it contains a variety of content. This can include articles, stories, photographs, and advertisements.</p>
  <footer class="footer footer--orange">
    <span class="contact contact--web"><svg><use href="#i-globe"/></svg>www.kestrelworks.example</span>
    <span class="contact contact--address"><svg><use href="#i-pin"/></svg>48 Foundry Lane, Eastbrook</span>
    <span class="contact contact--phone"><svg><use href="#i-phone"/></svg>+1-555-014-2280</span>
    <span class="contact contact--mail"><svg><use href="#i-mail"/></svg>hello@kestrelworks.example</span>
  </footer>
</section>

<!-- Page 3 : cooperation -->
<section class="page page--cooperation">
  <div class="photo" role="img" aria-label="Photo: smiling colleagues gathered around a laptop in a bright office" style="left:0;top:92px;width:538px;height:283px;background:linear-gradient(120deg,#d9cbb8,#b89a80 40%,#8d6e5a 70%,#c4b3a0)"></div>
  <svg class="shapes" viewBox="0 0 538 760" aria-hidden="true">
    <polygon points="250,20 538,20 538,92 262,92" fill="var(--orange)"/>
    <polygon points="0,17 255,17 285,100 0,100" fill="var(--black)"/>
    <polygon points="312,17 322,0 330,17" fill="var(--blue)"/>
    <polygon points="322,0 334,0 376,66 366,70" fill="var(--black)"/>
  </svg>
  <div class="brand brand--band">Kestrel Works</div>
  <div class="page-number">03</div>
  <h2 class="section-heading coop-heading">Our Most<br>Important<br>Cooperation</h2>
  <p class="body-copy" style="top:403px">A magazine is a periodical publication, which can either be printed or published electronically. It is issued regularly, usually every week or every month, and it contains a variety of content. This can include articles, stories, photographs, and advertisements.</p>
  <p class="body-copy" style="top:457px">To create your own, choose a topic that interests you. It can be anything from fashion and beauty to travel and the news. Once you have your overall theme, you can start brainstorming the content. Just starting? Design a memorable masthead with an equally memorable name.</p>
  <div class="feature feature--one">
    <h3>Teamwork 1</h3>
    <p>A magazine is a periodical publication, which can either be printed or published electronically.</p>
  </div>
  <div class="feature feature--two">
    <h3>Teamwork 2</h3>
    <p>A magazine is a periodical publication, which can either be printed or published electronically.</p>
  </div>
  <footer class="footer footer--orange">
    <span class="contact contact--web"><svg><use href="#i-globe"/></svg>www.kestrelworks.example</span>
    <span class="contact contact--address"><svg><use href="#i-pin"/></svg>48 Foundry Lane, Eastbrook</span>
    <span class="contact contact--phone"><svg><use href="#i-phone"/></svg>+1-555-014-2280</span>
    <span class="contact contact--mail"><svg><use href="#i-mail"/></svg>hello@kestrelworks.example</span>
  </footer>
</section>

<!-- Page 4 : team -->
<section class="page page--team">
  <svg class="shapes" viewBox="0 0 538 760" aria-hidden="true">
    <polygon points="250,20 538,20 538,92 262,92" fill="var(--orange)"/>
    <polygon points="0,17 255,17 285,100 0,100" fill="var(--black)"/>
    <polygon points="312,17 322,0 330,17" fill="var(--blue)"/>
    <polygon points="322,0 334,0 376,66 366,70" fill="var(--black)"/>
  </svg>
  <div class="brand brand--band">Kestrel Works</div>
  <div class="page-number">04</div>
  <h2 class="section-heading team-heading">Meet Our Team</h2>

  <div class="member col-a row-a"><div class="portrait" role="img" aria-label="Portrait photo of team member" style="background:linear-gradient(160deg,#a88468,#e3d2c0)"></div><div class="name">Nadia Marsh</div><div class="role">Owner</div></div>
  <div class="member col-b row-a"><div class="portrait" role="img" aria-label="Portrait photo of team member" style="background:linear-gradient(160deg,#c9c9c9,#3c4656)"></div><div class="name">Arlo Brandt</div><div class="role">Owner</div></div>
  <div class="member col-c row-a"><div class="portrait" role="img" aria-label="Portrait photo of team member" style="background:linear-gradient(160deg,#8c7a68,#1f4a46)"></div><div class="name">Ines Carvalho</div><div class="role">Owner</div></div>
  <div class="member col-a row-b"><div class="portrait" role="img" aria-label="Portrait photo of team member" style="background:linear-gradient(160deg,#d4d6dc,#2c3f73)"></div><div class="name">Tomas Reid</div><div class="role">Deputy Manager</div></div>
  <div class="member col-b row-b"><div class="portrait" role="img" aria-label="Portrait photo of team member" style="background:linear-gradient(160deg,#7d5e47,#8fa8c4)"></div><div class="name">Marcus Doyle</div><div class="role">Manager</div></div>
  <div class="member col-c row-b"><div class="portrait" role="img" aria-label="Portrait photo of team member" style="background:linear-gradient(160deg,#4a3224,#c99a78)"></div><div class="name">Elena Voss</div><div class="role">Deputy Manager</div></div>

  <footer class="footer footer--orange">
    <span class="contact contact--web"><svg><use href="#i-globe"/></svg>www.kestrelworks.example</span>
    <span class="contact contact--address"><svg><use href="#i-pin"/></svg>48 Foundry Lane, Eastbrook</span>
    <span class="contact contact--phone"><svg><use href="#i-phone"/></svg>+1-555-014-2280</span>
    <span class="contact contact--mail"><svg><use href="#i-mail"/></svg>hello@kestrelworks.example</span>
  </footer>
</section>

<!-- Page 5 : closing -->
<section class="page page--closing">
  <svg class="shapes" viewBox="0 0 538 760" aria-hidden="true">
    <polygon points="362,113 412,31 446,113" fill="var(--blue)"/>
    <polygon points="0,100 113,100 248,445 0,445" fill="var(--orange)"/>
    <polygon points="240,412 282,412 250,445" fill="var(--blue)"/>
  </svg>
  <svg class="photo" style="left:0;top:0" width="538" height="760" viewBox="0 0 538 760" role="img" aria-label="Photo: glass office tower seen from below with autumn trees">
    <polygon points="118,113 538,113 538,412 240,412" fill="url(#g-sky)"/>
  </svg>
  <svg class="shapes" viewBox="0 0 538 760" aria-hidden="true">
    <polygon points="412,31 470,31 538,150 538,262" fill="var(--orange)"/>
  </svg>
  <div class="brand brand--cover">Kestrel Works</div>
  <div class="kicker" style="top:468px;font-size:15px">End Of Proposal</div>
  <div class="kicker-rule" style="left:190px;top:478px;width:46px"></div>
  <div class="title-xl" style="top:495px;font-size:46px;font-weight:900">THANK<br>YOU</div>
  <p class="lead" style="top:606px;width:365px;font-size:11px;line-height:16.5px">A magazine is a periodical publication, which can either be printed or published electronically. It is issued regularly, usually every week or every month, and it contains a variety of content.</p>
  <footer class="footer footer--dark">
    <span class="contact contact--web"><svg><use href="#i-globe"/></svg>www.kestrelworks.example</span>
    <span class="contact contact--address"><svg><use href="#i-pin"/></svg>48 Foundry Lane, Eastbrook</span>
    <span class="contact contact--phone"><svg><use href="#i-phone"/></svg>+1-555-014-2280</span>
    <span class="contact contact--mail"><svg><use href="#i-mail"/></svg>hello@kestrelworks.example</span>
  </footer>
</section>

</body>
</html>
```